AUSTRALIAN CONSULTING FIRM BUSINESS CARD - MODERN

We are wanting a modern, clean lined business card design. We are professional niche consultancy firm situated in Australia called Marlow Advisory Partners Pty Ltd.
The card should communicate professionalism and creativity and draw on our logo design (attached).
The design should be two sided, landscape orientation.
Target Market(s)
government, not for profit sector, corporate clients
Industry/Entity Type
Landscape
Requirements
Must have
- logo
no new introduced colours

```html
<!DOCTYPE html>
<html lang="en">
<head>
<meta charset="utf-8">
<title>Marlow Advisory Partners – Business Card</title>
<link rel="stylesheet" href="https://fonts.googleapis.com/css2?family=Open+Sans:wght@300;400;600;800&display=swap">
<style>
  :root {
    --brand-blue: #1c3f98;
    --brand-blue-deep: #16347f;
    --brand-cyan: #1ba3e0;
    --brand-purple: #b03ea6;
    --brand-green: #7dc43c;
    --paper: #ffffff;
    --stage: #e9ebef;
    --ink-light: #ffffff;
  }
  * { box-sizing: border-box; margin: 0; padding: 0; }
  html, body {
    width: 1200px;
    height: 1024px;
    overflow: hidden;
    background: var(--stage);
    font-family: "Open Sans", Arial, sans-serif;
  }
  .card {
    position: absolute;
    left: 190px;
    width: 820px;
    height: 468px;
    overflow: hidden;
    box-shadow: 0 6px 18px rgba(20, 30, 60, 0.18);
  }
  .card--front { top: 29px; background: var(--paper); }
  .card--back  { top: 526px; background: var(--brand-blue); }

  .front-shape { position: absolute; inset: 0; }

  .wordmark {
    position: absolute;
    font-weight: 800;
    text-transform: uppercase;
    line-height: 1.1;
    letter-spacing: 0.5px;
    white-space: nowrap;
  }
  .wordmark__dot {
    position: absolute;
    border-radius: 50%;
    background: var(--brand-cyan);
  }
  .card--front .wordmark {
    left: 84px;
    top: 236px;
    font-size: 23px;
    color: var(--brand-blue);
  }
  .card--front .wordmark__dot {
    left: 36px; top: 242px; width: 36px; height: 36px;
  }

  .contact {
    position: absolute;
    right: 40px;
    top: 36px;
    width: 340px;
    text-align: right;
    color: var(--ink-light);
  }
  .contact__name {
    font-weight: 300;
    font-size: 24px;
    letter-spacing: 1px;
    text-transform: uppercase;
    color: var(--brand-green);
  }
  .contact__title {
    font-size: 13px;
    margin-bottom: 40px;
  }
  .contact__address {
    font-size: 17px;
    line-height: 1.35;
    margin-bottom: 22px;
  }
  .contact__line {
    display: flex;
    justify-content: flex-end;
    align-items: center;
    gap: 10px;
    font-size: 17px;
    line-height: 1.6;
  }
  .contact__line svg { width: 15px; height: 15px; flex: none; }

  .card--back .wordmark {
    right: 48px;
    top: 258px;
    font-size: 38px;
    text-align: right;
    color: var(--ink-light);
  }
  .card--back .wordmark__dot {
    left: 70px; top: 90px; width: 70px; height: 70px;
  }
  .back-web {
    position: absolute;
    right: 48px;
    top: 360px;
    font-size: 18px;
    font-weight: 600;
    color: var(--brand-green);
  }
</style>
</head>
<body>

<section class="card card--front">
  <svg class="front-shape" viewBox="0 0 820 468" aria-hidden="true">
    <path d="M430 0 Q 380 234 470 468 L820 468 L820 0 Z" fill="var(--brand-blue)"/>
    <path d="M430 0 Q 380 234 470 468 L452 468 Q 362 234 414 0 Z" fill="var(--brand-purple)"/>
    <path d="M406 0 Q 354 234 444 468 L438 468 Q 348 234 400 0 Z" fill="var(--brand-green)"/>
  </svg>

  <span class="wordmark__dot"></span>
  <div class="wordmark">Marlow Advisory<br>Partners Pty Ltd</div>

  <div class="contact">
    <p class="contact__name">Elliot Varga</p>
    <p class="contact__title">Job Title</p>
    <p class="contact__address">Your address goes here,<br>city, zip code, country name</p>
    <p class="contact__line">000-000-000
      <svg viewBox="0 0 16 16"><path d="M4 1h3l1 4-2 1a8 8 0 0 0 4 4l1-2 4 1v3c0 1-1 2-2 2A13 13 0 0 1 2 3c0-1 1-2 2-2z" fill="var(--brand-green)"/></svg>
    </p>
    <p class="contact__line">000-000-000
      <svg viewBox="0 0 16 16"><rect x="2" y="5" width="12" height="9" rx="1" fill="var(--brand-green)"/><rect x="4" y="2" width="8" height="4" fill="var(--brand-green)"/></svg>
    </p>
    <p class="contact__line">name@domainname.com
      <svg viewBox="0 0 16 16"><rect x="1" y="3" width="14" height="10" rx="1" fill="var(--brand-green)"/><path d="M1 4l7 5 7-5" stroke="var(--brand-blue)" stroke-width="1.5" fill="none"/></svg>
    </p>
    <p class="contact__line">www.websitename.com
      <svg viewBox="0 0 16 16"><circle cx="8" cy="8" r="7" fill="var(--brand-green)"/><path d="M1 8h14M8 1c-3 4-3 10 0 14M8 1c3 4 3 10 0 14" stroke="var(--brand-blue)" stroke-width="1" fill="none"/></svg>
    </p>
  </div>
</section>

<section class="card card--back">
  <span class="wordmark__dot"></span>
  <div class="wordmark">Marlow Advisory<br>Partners Pty Ltd</div>
  <p class="back-web">www.websitename.com</p>
</section>

</body>
</html>
```